Business Card Design Project

Business card design with a funky, clean, modern design. Business is an immigration consultancy. Client base will be Canadian employers wanting to hire or retain foreign workers and foreign nationals wanting to immigrate to Canada.

Full color possible, but should incorporate red/white/black as per the logo to be provided. Double sided card design.

Target Market(s)

Canadian employers looking to hire/retain staff and also foreign nationals immigrating to Canada

Industry/Entity Type

Business

Requirements
Must have
• Logo (to be provided)
Name (Marla Voskuil, Immigration Consultant)
Phone (604) 731-5562
E-mail: marla@tallowbrookmigration.example
Web: www.tallowbrookmigration.example

Nice to have
• Tag Line
Clean, modern style

```html
<!DOCTYPE html>
<html lang="en">
<head>
<meta charset="utf-8">
<title>Tallowbrook Migration – Business Card</title>
<link rel="stylesheet" href="https://fonts.googleapis.com/css2?family=Lato:wght@400;700&display=swap">
<style>
  :root {
    --backdrop: #e4e7e9;
    --card-white: #ffffff;
    --card-charcoal: #2a2a2c;
    --ink: #2b2b2b;
    --brand-red: #e0141e;
    --shadow: rgba(0, 0, 0, 0.18);
  }
  * { box-sizing: border-box; margin: 0; padding: 0; }
  html, body {
    width: 1200px;
    height: 960px;
    overflow: hidden;
    background: var(--backdrop);
    font-family: "Lato", Arial, sans-serif;
  }
  .sheet {
    position: relative;
    width: 1200px;
    height: 960px;
  }
  .card {
    position: absolute;
    left: 280px;
    width: 640px;
    height: 366px;
    box-shadow: 0 10px 30px var(--shadow);
    overflow: hidden;
  }
  .card--front { top: 80px; background: var(--card-white); }
  .card--back  { top: 514px; background: var(--card-charcoal); }

  .holder { position: absolute; left: 58px; top: 70px; color: var(--ink); }
  .holder__name { font-size: 30px; font-weight: 400; line-height: 1.2; }
  .holder__title { font-size: 25px; font-weight: 400; line-height: 1.3; margin-top: 4px; }

  .contact {
    position: absolute;
    left: 40px;
    top: 196px;
    list-style: none;
    color: var(--ink);
    font-size: 18px;
  }
  .contact__item { display: flex; align-items: center; gap: 12px; height: 28px; }
  .contact__icon { width: 14px; height: 14px; flex: none; }

  .web-band {
    position: absolute;
    left: 0;
    top: 290px;
    width: 356px;
    height: 30px;
    background: var(--brand-red);
    color: var(--card-white);
    font-size: 16px;
    line-height: 30px;
    padding-left: 40px;
    white-space: nowrap;
  }

  .brand {
    position: absolute;
    right: 34px;
    top: 70px;
    width: 210px;
    display: flex;
    flex-direction: column;
    align-items: center;
  }
  .brand__dot {
    width: 120px;
    height: 120px;
    border-radius: 50%;
    background: var(--brand-red);
  }
  .brand__name {
    margin-top: 22px;
    font-size: 24px;
    font-weight: 700;
    color: var(--ink);
    text-align: center;
    line-height: 1.15;
    letter-spacing: 1px;
  }

  .back-brand {
    position: absolute;
    inset: 0;
    display: flex;
    flex-direction: column;
    align-items: center;
    justify-content: center;
  }
  .back-brand__dot {
    width: 170px;
    height: 170px;
    border-radius: 50%;
    background: var(--brand-red);
  }
  .back-brand__name {
    margin-top: 26px;
    font-size: 30px;
    font-weight: 700;
    letter-spacing: 2px;
    color: var(--card-white);
  }
</style>
</head>
<body>
<main class="sheet">
  <section class="card card--front" aria-label="Card front">
    <div class="holder">
      <p class="holder__name">Marla Voskuil</p>
      <p class="holder__title">RCIC</p>
    </div>
    <ul class="contact">
      <li class="contact__item">
        <svg class="contact__icon" viewBox="0 0 14 14" aria-hidden="true">
          <path d="M1 5 Q7 0 13 5 L11 6.5 L9.5 4.5 L4.5 4.5 L3 6.5 Z" fill="var(--brand-red)"/>
          <rect x="2.5" y="7" width="9" height="6" rx="1" fill="var(--brand-red)"/>
          <circle cx="7" cy="10" r="1.6" fill="var(--card-white)"/>
        </svg>
        <span>(604) 731-5562</span>
      </li>
      <li class="contact__item">
        <svg class="contact__icon" viewBox="0 0 14 14" aria-hidden="true">
          <rect x="1" y="3" width="12" height="9" rx="1" fill="var(--brand-red)"/>
          <path d="M1.5 3.8 L7 8 L12.5 3.8" fill="none" stroke="var(--card-white)" stroke-width="1.2"/>
        </svg>
        <span>marla@tallowbrookmigration.example</span>
      </li>
    </ul>
    <div class="web-band">www.tallowbrookmigration.example</div>
    <div class="brand">
      <span class="brand__dot" aria-hidden="true"></span>
      <p class="brand__name">TALLOWBROOK MIGRATION</p>
    </div>
  </section>

  <section class="card card--back" aria-label="Card back">
    <div class="back-brand">
      <span class="back-brand__dot" aria-hidden="true"></span>
      <p class="back-brand__name">TALLOWBROOK MIGRATION</p>
    </div>
  </section>
</main>
</body>
</html>
```